Logo and Business card design!

Halvern Estates

We are a Property development and real estate company (needs a logo design).

Halvern estates is based in Sydney Australia and will be dealing with high net worth individuals with a corporate background. The demographic of clients will be relatively youthful and savvy. We do development finance, property development and some portion of property sales

I'd like the 'Halvern' part of the name to be strength of the title, with 'property' playing a very minor part, perhaps in tiny font somewhere off to the bottom or side or something

Thank you!

Target Market(s)

25-55 years old

Industry/Entity Type

Real Estate Development

Contact Information for Business Card

Please arrange this information as you see fit

Doug Pennicott
Managing Director
0417 582 330
doug@halvernestates.com.au
www.halvernestates.com.au

Logo Text

Halvern estates

Font styles to use
Serif

Colors

Designer to choose colors to be used in the design.

Requirements
Must have
• PLEASE VIEW THE UPLOADED IMAGES AND EXAMPLES
• And please put 'property' in small letters at the bottom or to the side. I want it to play a minimalist role, with 'HALVERN' being the feature
• Colours! Please make sure theyre mostly grey and white with possibly some other dark blue and maybe dark grey
Nice to have
• Please feel free to use whatever colors you like, the suggested colors are something I selected momentarily and dont necessarily reflect strict guidelines
Should not have
• NO pictures or shapes of houses. I dont want the logo design to be so literal in its imagery

```html
<!DOCTYPE html>
<html lang="en">
<head>
<meta charset="utf-8">
<title>Halvern Estates — Business Card</title>
<link rel="stylesheet" href="https://fonts.googleapis.com/css2?family=Cinzel:wght@400;700&family=Open+Sans:wght@400&display=swap">
<style>
  :root {
    --backdrop: #313131;
    --card-light: #f2f2f2;
    --brand-green: #3d8f00;
    --ink-dark: #141414;
    --ink-body: #333333;
    --ink-white: #ffffff;
  }
  * { margin: 0; padding: 0; box-sizing: border-box; }
  html, body {
    width: 1200px; height: 900px; overflow: hidden;
    background: var(--backdrop);
  }
  .stage { position: relative; width: 1200px; height: 900px; }
  .card {
    position: absolute; top: 170px; width: 347px; height: 561px;
    text-align: center;
  }
  .card--front { left: 259px; background: var(--card-light); }
  .card--back { left: 631px; background: var(--brand-green); }

  .wordmark { position: absolute; left: 0; right: 0; font-family: "Cinzel", serif; font-weight: 400; }
  .wordmark__name { display: block; font-size: 47px; line-height: 1; letter-spacing: 1px; }
  .wordmark__tag { display: block; font-size: 16px; letter-spacing: 17px; margin-top: 14px; padding-left: 17px; }
  .card--front .wordmark { top: 218px; color: var(--ink-dark); }
  .card--back .wordmark { top: 322px; color: var(--ink-white); }

  .contact { position: absolute; left: 0; right: 0; top: 370px; }
  .contact__name {
    font-family: "Cinzel", serif; font-weight: 700; font-size: 18px;
    color: var(--brand-green); letter-spacing: 0.5px;
  }
  .contact__role, .contact__line {
    font-family: "Open Sans", sans-serif; font-size: 14.5px; color: var(--ink-body);
  }
  .contact__role { margin-top: 1px; }
  .contact__icons { display: flex; justify-content: center; gap: 6px; margin-top: 31px; margin-bottom: 9px; }
  .contact__icons svg { width: 13px; height: 13px; fill: var(--brand-green); }
  .contact__line { line-height: 21px; }
</style>
</head>
<body>
<main class="stage">
  <section class="card card--front">
    <div class="wordmark">
      <span class="wordmark__name">HALVERN</span>
      <span class="wordmark__tag">ESTATES</span>
    </div>
    <div class="contact">
      <p class="contact__name">DOUG PENNICOTT</p>
      <p class="contact__role">Managing Director</p>
      <div class="contact__icons" aria-hidden="true">
        <svg viewBox="0 0 16 16"><path d="M3.5 1.2l2.4 2.9-1.3 1.8c.9 2 2.5 3.6 4.5 4.5l1.8-1.3 2.9 2.4-1.2 2.2C7 13.4 2.6 9 1.3 2.4z"/></svg>
        <svg viewBox="0 0 16 16"><path d="M1 3h14v10H1z M1.8 3.6L8 8.5l6.2-4.9" stroke="#f2f2f2" stroke-width="1"/></svg>
        <svg viewBox="0 0 16 16"><circle cx="8" cy="8" r="7"/><path d="M1 8h14M8 1c-3 3.5-3 10.5 0 14M8 1c3 3.5 3 10.5 0 14" stroke="#f2f2f2" stroke-width="1" fill="none"/></svg>
      </div>
      <p class="contact__line">0417 582 330</p>
      <p class="contact__line">doug@halvernestates.com.au</p>
      <p class="contact__line">www.halvernestates.com.au</p>
    </div>
  </section>

  <section class="card card--back">
    <div class="wordmark">
      <span class="wordmark__name">HALVERN</span>
      <span class="wordmark__tag">ESTATES</span>
    </div>
  </section>
</main>
</body>
</html>
```